REAL PSYCHIC rear window decal. Mystical, light, positive, spiritual coach vibes

Design a sign for my back car window.
HOT PINK and purple swirly, mystical sign. Eye-catching and classy.
Size 24” x 18”
TEXT:
MARLENE DOVE
Psychic & Medium
Www,.marlenedove.com
World Renowned for Over 45 Years. (This last line make small at bottom)

*This is not a filled in magnet, it will be transparent.

Target Market(s)

Women

Industry/Entity Type

Spirituality

Font styles to use
Script
Other font styles liked:
• See upload for a font I like

Colors
E54698
E96AAD
F1A4CE
F9D9EA
FCEFF6
A7469A
B969AE
D3A5CF
EDDBEB
F8F0F9
6B429C
8869AF
B7A5CE
E3DAEB
F3F0F8

Requirements
Must have
• Pink purple, classy yet mystical vibe
Nice to have
• Easy to read, but old-timey classic font for “MARLENE DOVE”

```html
<!DOCTYPE html>
<html lang="en">
<head>
<meta charset="utf-8">
<title>Marlene Dove – Psychic &amp; Medium Window Decal</title>
<link rel="stylesheet" href="https://fonts.googleapis.com/css2?family=Great+Vibes&family=Berkshire+Swash&family=Playfair+Display:wght@700&display=swap">
<style>
  :root {
    --hot-pink: #e96aad;
    --soft-pink: #f9d9ea;
    --blush: #fcebf5;
    --deep-purple: #6b429c;
    --mid-purple: #8869af;
    --lavender: #b7a5ce;
    --aqua: #3bc4e6;
    --frame-grey: #b5b5b5;
    --paper: #ffffff;
  }
  html, body {
    margin: 0;
    padding: 0;
    width: 1200px;
    height: 1200px;
    overflow: hidden;
    background: var(--paper);
  }
  .decal {
    display: block;
    width: 1200px;
    height: 1200px;
  }
  .decal-frame {
    fill: none;
    stroke: var(--frame-grey);
    stroke-width: 1.5;
  }
  .client-name {
    font-family: "Great Vibes", cursive;
    font-size: 190px;
    fill: var(--hot-pink);
  }
  .service-title {
    font-family: "Berkshire Swash", cursive;
    font-size: 64px;
    fill: var(--deep-purple);
  }
  .website {
    font-family: "Playfair Display", serif;
    font-weight: 700;
    font-size: 31px;
    letter-spacing: 1px;
    fill: var(--mid-purple);
  }
  .tagline {
    font-family: "Great Vibes", cursive;
    font-size: 84px;
    fill: var(--mid-purple);
  }
</style>
</head>
<body>
<svg class="decal" viewBox="0 0 1200 1200" xmlns="http://www.w3.org/2000/svg">
  <defs>
    <radialGradient id="eyes-glow" cx="50%" cy="50%" r="50%">
      <stop offset="0%" stop-color="#f9d9ea"/>
      <stop offset="55%" stop-color="#e3daeb"/>
      <stop offset="100%" stop-color="#ffffff" stop-opacity="0"/>
    </radialGradient>
    <path id="title-arc" d="M318 820 Q600 650 884 826"/>
    <path id="website-arc" d="M404 834 Q600 792 798 846"/>
  </defs>

  <rect class="decal-frame" x="78" y="208" width="1044" height="784"/>

  <text class="client-name" x="148" y="466" textLength="950" lengthAdjust="spacingAndGlyphs">Marlene Dove</text>

  <rect class="eyes-artwork" x="170" y="505" width="870" height="170" rx="85"
        fill="url(#eyes-glow)" role="img"
        aria-label="Illustration of two mystical eyes with purple brows, pink lids, turquoise irises and sparkles"/>

  <text class="service-title">
    <textPath href="#title-arc" startOffset="50%" text-anchor="middle">Psychic &amp; Medium</textPath>
  </text>

  <text class="website">
    <textPath href="#website-arc" startOffset="50%" text-anchor="middle">www.marlenedove.com</textPath>
  </text>

  <text class="tagline" x="128" y="956" textLength="942" lengthAdjust="spacingAndGlyphs">World Renowned for Over 45 years</text>
</svg>
</body>
</html>
```